Website Design for a Party Rental
Brinmore Party Rentals
Project: Website Design for a Party Rental
Website Design for a Party Rental - Events
Creative Brief
Events
http://www.brinmorepartyrentals-example.com/
Its a family owned party rental company, that rents from chairs, table, linen, china, flatware, to tenting, dance floor & lighting. We rent for any sort of event, from casual birthday parties, wedding, to the Pacific Motorwheel Expo in Harbin Dome Arena. Our prices are cheaper than our nearby competitors. We do free consultations on site, therefore providing a quote if client wishes to confirm with us.
Likes: Oak & Meadow Rentals http://www.oakandmeadoweventhire-example.com/ We Like the Inventory Layout of this website, and how its organized. Also, the Slide show above the header.
Modern
Cobalt Blue (Its like a Ocean/Royal Blue)
http://www.oakandmeadoweventhire-example.com/
http://losangeles.vintelpartyhire-example.com/

```html
<!DOCTYPE html>
<html lang="en">
<head>
<meta charset="utf-8">
<title>Brinmore Party Rentals</title>
<link href="https://fonts.googleapis.com/css2?family=Open+Sans:wght@400;600;700&family=Libre+Baskerville:wght@400;700&display=swap" rel="stylesheet">
<style>
  :root {
    --page-bg: #3b4150;
    --page-bg-dark: #2f3440;
    --white: #ffffff;
    --teal: #1f8088;
    --teal-dark: #16636a;
    --ink: #333a44;
    --nav-ink: #3d434d;
    --panel: #4a4e55;
    --panel-inner: #5d6269;
    --footer: #2b2e33;
    --footer-ink: #9a9ea5;
    --photo-a: #c9a2c9;
    --photo-b: #7b5a86;
  }
  * { margin: 0; padding: 0; box-sizing: border-box; }
  html, body { width: 1200px; height: 1093px; overflow: hidden; }
  body {
    position: relative;
    background: linear-gradient(135deg, var(--page-bg), var(--page-bg-dark));
    font-family: "Open Sans", sans-serif;
  }
  .site { position: absolute; left: 124px; top: 0; width: 957px; height: 1093px; }
  .header { position: absolute; left: 0; top: 0; width: 957px; height: 420px; background: var(--white); }

  .brand { position: absolute; left: 30px; top: 60px; width: 400px; text-align: center; }
  .brand-mark { width: 120px; height: 120px; border-radius: 50%; background: var(--teal); margin: 0 auto 30px; }
  .brand-name { font-family: "Open Sans", sans-serif; font-weight: 700; font-size: 40px; color: var(--teal); letter-spacing: -0.5px; }
  .brand-phone { font-family: "Libre Baskerville", serif; font-size: 50px; color: var(--ink); letter-spacing: 2px; margin-top: 14px; }

  .top-links { position: absolute; left: 430px; top: 22px; font-size: 16px; font-weight: 700; color: var(--ink); }
  .top-links span { margin: 0 6px; }
  .top-links .current { text-decoration: underline; }
  .search { position: absolute; left: 682px; top: 18px; width: 195px; height: 28px; border: 1px solid #bbb; border-radius: 3px; font-size: 12px; color: #888; padding: 5px 8px; background: #f6f6f6; }

  .slideshow { position: absolute; left: 424px; top: 53px; width: 468px; height: 317px; border: 6px solid #222; background: linear-gradient(160deg, var(--photo-a), var(--photo-b) 55%, #e9e3dc); }
  .dots { position: absolute; left: 612px; top: 382px; display: flex; gap: 10px; }
  .dots i { width: 10px; height: 10px; border-radius: 50%; background: #999; display: block; }
  .dots i:first-child { background: #444; }

  .main-nav { position: absolute; left: 0; top: 424px; width: 957px; height: 66px; background: linear-gradient(#ffffff, #e6e8ea); border-top: 5px solid var(--teal); border-bottom: 5px solid var(--teal); display: flex; align-items: center; justify-content: center; gap: 20px; font-family: "Libre Baskerville", serif; font-weight: 700; font-size: 30px; color: var(--nav-ink); }
  .main-nav .active { color: var(--teal); text-decoration: underline; }
  .main-nav .sep { color: #aaa; font-weight: 400; }
  .main-nav .caret { font-size: 16px; color: var(--teal); }

  .content { position: absolute; left: 0; top: 504px; width: 957px; height: 430px; background: var(--panel); }
  .content-inner { position: absolute; left: 38px; top: 22px; width: 880px; height: 390px; background: var(--panel-inner); color: var(--white); text-align: center; padding: 14px 30px; }
  .content h1 { font-size: 27px; font-weight: 700; line-height: 1.1; }
  .content .lead { font-size: 21px; font-weight: 600; line-height: 1.2; margin-top: 2px; }
  .content h2 { font-size: 20px; font-weight: 600; margin-top: 22px; }
  .content p { font-size: 19px; line-height: 1.23; margin-top: 4px; }

  .footer { position: absolute; left: 0; top: 972px; width: 957px; height: 121px; background: var(--footer); }
  .footer-nav { position: absolute; left: 22px; top: 12px; display: flex; gap: 32px; font-family: "Libre Baskerville", serif; font-size: 14px; letter-spacing: 1px; color: var(--footer-ink); }
  .footer-nav .active { color: var(--white); }
  .newsletter { position: absolute; left: 24px; top: 48px; width: 325px; height: 73px; background: #3b3f46; padding: 6px 10px; }
  .newsletter h3 { font-family: "Libre Baskerville", serif; font-weight: 400; font-size: 12px; letter-spacing: 1px; color: var(--footer-ink); }
  .social { position: absolute; left: 10px; top: 34px; display: flex; gap: 6px; }
  .social i { display: block; width: 20px; height: 20px; border-radius: 3px; background: #6c7582; }
  .email { position: absolute; left: 110px; top: 32px; width: 200px; height: 24px; border-bottom: 1px solid #777; font-size: 12px; color: var(--footer-ink); padding: 4px; }
  .address { position: absolute; left: 420px; top: 48px; width: 200px; text-align: center; font-family: "Libre Baskerville", serif; font-style: italic; font-size: 11px; line-height: 1.3; color: var(--footer-ink); }
  .recent { position: absolute; left: 680px; top: 44px; width: 250px; }
  .recent h3 { font-family: "Libre Baskerville", serif; font-style: italic; font-weight: 400; font-size: 19px; color: var(--white); text-align: center; }
  .thumbs { display: grid; grid-template-columns: repeat(3, 1fr); gap: 5px; margin-top: 4px; }
  .thumbs div { height: 20px; background: linear-gradient(135deg, #b56a9a, #4d3b6a); }
</style>
</head>
<body>
  <div class="site">
    <header class="header">
      <div class="brand">
        <div class="brand-mark"></div>
        <div class="brand-name">Brinmore Party Rentals</div>
        <div class="brand-phone">310·555·0148</div>
      </div>
      <nav class="top-links"><span class="current">About us</span>|<span>Portfolio</span>|<span>Blog</span></nav>
      <div class="search">Search Keywords</div>
      <div class="slideshow" role="img" aria-label="Slideshow photo of a tent interior draped in purple fabric with dressed banquet tables"></div>
      <div class="dots"><i></i><i></i><i></i><i></i><i></i></div>
    </header>

    <nav class="main-nav">
      <span class="active">Home</span><span class="sep">|</span>
      <span>Services <span class="caret">▾</span></span><span class="sep">|</span>
      <span>Catalog <span class="caret">▾</span></span><span class="sep">|</span>
      <span>Price list</span><span class="sep">|</span>
      <span>Contact us</span>
    </nav>

    <section class="content">
      <div class="content-inner">
        <h1>Let Our Wide Range of Rentals Help Your Event</h1>
        <div class="lead">When it comes to party rentals Los Angeles knows how to get it done! You can count on Brinmore Party Rentals to outfit your event with style. Give us a call today!</div>
        <h2>We’ll Outfit Your Event with Quality Party Rentals in Los Angeles</h2>
        <p>Don’t break your budget when you’re preparing for your next party! Rely on the party rentals Los Angeles trusts for a fun and fancy event. At Brinmore Party Rentals, we pride ourselves on offering the best customer service, as well as the best rental products to the residents of Los Angeles. When it comes to party rentals in Los Angeles, we know that there is a high standard regarding how events should be pulled off. At the same time, we also understand that not everyone has the budget to spend big bucks. We offer the products that are still elegant, but competitively priced.</p>
      </div>
    </section>

    <footer class="footer">
      <nav class="footer-nav">
        <span class="active">Home</span><span>Services</span><span>Catalog</span><span>Price list</span><span>Contact us</span><span>About us</span><span>Portfolio</span><span>Blog</span>
      </nav>
      <div class="newsletter">
        <h3>Subscribe to our newsletter</h3>
        <div class="social"><i></i><i></i><i></i></div>
        <div class="email">Email address</div>
      </div>
      <div class="address">
        4820 Marlow Ave<br>Los Angeles, CA 90066<br><br>
        Monday – Friday: 9 am – 6 pm<br>Saturday: 9 am – 5 pm<br>Sunday Closed
      </div>
      <div class="recent">
        <h3>Recent parties</h3>
        <div class="thumbs" role="img" aria-label="Thumbnail photos of recent decorated events">
          <div></div><div></div><div></div><div></div><div></div><div></div>
        </div>
      </div>
    </footer>
  </div>
</body>
</html>
```